Modern home page design for insurance and investment business

- The design should be based around the attached HPID (home page information design) called KRT HPID. The table boxes are just for approximate placement of information – you DON'T have to make it look exactly like this.
- Information only is in orange text. Copy to go on the design in black text. Some instructions are in the HPID. Please be creative! You don’t have to use the exact images provided if you have a better idea.

- The design needs to be clean and spacious. Please use the colours from the logos in the website design. Lots of white too.

I've attached home page gallery example photos. You can use any of these photos or something similar with the words from one of the photos.

- Expected standard of design examples: (Please DO NOT copy these exactly – they are just examples)
http://www.brackenvale.example.nz/
https://www.tarnwick.example.nz/
http://quillmoorcover.example.nz/homepage/

Width of content will be 1100 pixels when implemented as a web page. Header height (without nav bar) 150-160 pixels.

The winning PSD file will have to be provided as follows…
1. Canvas size of 2000px x 2000px - 72ppi in Adobe Photoshop (CS5 compatible)
2. Width of content section is 1100px wide - centered in the canvas
3. Any button rollovers/hovers in the PSD as hidden layers.
4. All fonts used must be Google fonts (except for the fonts in the header at the top of the page).
5. You will need to supply the chosen home page plus one example page (example page as a style guide for how all other pages will look). Example page is only the header and navigational bar at the top, an empty sector in the middle with a column (180 px wide) which can be left or right aligned which means the main sector is 920 pixels wide, and then the footer at the bottom of the page.

```html
<!DOCTYPE html>
<html lang="en">
<head>
<meta charset="utf-8">
<title>KRT Insure &amp; Invest</title>
<link href="https://fonts.googleapis.com/css2?family=Open+Sans:wght@400;600;700&display=swap" rel="stylesheet">
<style>
:root{
  --navy:#0b3a6e;
  --navy-deep:#072d58;
  --footer:#0b4a84;
  --footer-base:#0a4179;
  --sky:#bcd6f2;
  --sky-light:#d9e8f8;
  --text:#444;
  --head:#333;
  --pale:#eef4f8;
  --card:#f0f0f0;
  --link:#1d4f88;
  --white:#fff;
}
*{margin:0;padding:0;box-sizing:border-box}
html,body{width:773px;height:1200px;overflow:hidden}
body{font-family:"Open Sans",Arial,sans-serif;color:var(--text);background:var(--white);position:relative}
.abs{position:absolute}
/* header */
.header{left:0;top:0;width:773px;height:73px;background:linear-gradient(var(--sky-light),var(--sky));border-top:3px solid var(--navy)}
.brand{left:81px;top:14px;display:flex;align-items:center;gap:8px;font-size:30px;font-weight:700;color:var(--navy);letter-spacing:1px}
.brand-dot{width:26px;height:26px;border-radius:50%;background:var(--navy)}
.brand small{font-size:11px;font-weight:700;letter-spacing:.5px}
.nz-map{left:306px;top:7px;width:37px;height:58px;background:linear-gradient(160deg,#e9edd9,#c9d2b0);border-radius:40% 20% 40% 30%}
.region{font-size:9px;color:var(--link);white-space:nowrap}
.region b{color:var(--navy-deep)}
.tagline{right:70px;top:17px;text-align:right;font-size:9.5px;line-height:14.5px;color:var(--link)}
.nav{left:0;top:73px;width:773px;height:22px;background:var(--navy)}
.nav a{position:absolute;top:5px;font-size:8.8px;color:var(--white);text-decoration:none;white-space:nowrap}
/* hero */
.hero-band{left:0;top:95px;width:773px;height:208px;background:#d3d3d3}
.hero{left:59px;top:95px;width:654px;height:208px;background:linear-gradient(180deg,#e8eaec 0%,#cfd3d6 45%,#7b7e7a 100%)}
/* overview */
.overview{left:0;top:303px;width:773px;height:190px;background:var(--pale)}
.ov-title{font-size:17px;font-weight:400;color:var(--head);letter-spacing:.5px}
.ov-text{width:290px;font-size:8.4px;line-height:12.5px;color:var(--text)}
.divider{left:387px;top:343px;width:1px;height:120px;background:#d6dde3}
.btn{height:40px;width:143px;background:var(--navy);border:2px solid var(--link);outline:1px solid var(--navy);display:flex;align-items:center;gap:10px;padding-left:10px;color:var(--white);font-size:12px;font-weight:600;border-radius:2px}
/* life stage */
.stage-title{left:70px;top:516px;font-size:13px;font-weight:400;color:var(--head)}
.stage-rule{left:241px;top:529px;width:472px;height:1px;background:var(--navy)}
.card{width:149px;height:214px;top:552px;background:var(--card)}
.card h3{height:29px;background:var(--navy);color:var(--white);font-size:14px;font-weight:600;text-align:center;line-height:29px}
.card .photo{margin:4px auto 0;width:132px;height:88px;border-radius:44px 44px 30px 30px}
.card ul{list-style:none;padding:9px 8px 0 10px}
.card li{font-size:8.4px;line-height:10px;margin-bottom:8px;padding-left:8px;position:relative;color:#555}
.card li::before{content:"";position:absolute;left:0;top:2px;border-left:5px solid var(--navy);border-top:3px solid transparent;border-bottom:3px solid transparent}
/* callback form */
.form-bg{left:0;top:825px;width:773px;height:125px;background:linear-gradient(180deg,#dbe7f1,#c9dbe9 50%,#e4ecf2)}
.form-tab{left:59px;top:800px;width:474px;height:25px}
.form-tab span{position:absolute;left:12px;top:5px;font-size:12.5px;font-weight:600;color:var(--white);white-space:nowrap}
.field{background:var(--white);border:1px solid #d2d8dd;font-size:8.4px;color:#666;padding:6px 5px}
.send{left:551px;top:878px;width:142px;height:53px;background:var(--navy);border:3px solid var(--navy-deep);outline:1px solid var(--link);outline-offset:-6px;color:#dbe6f2;font-size:12px;letter-spacing:1px;display:flex;align-items:center;justify-content:center}
/* footer */
.footer{left:0;top:950px;width:773px;height:222px;background:var(--footer)}
.footer-base{left:0;top:1172px;width:773px;height:28px;background:var(--footer-base);border-top:1px solid #0d5294;font-size:8.4px;color:#93acc8;text-align:center;line-height:26px}
.f{font-size:9px;color:var(--white);white-space:nowrap}
.f.dim{color:#c6d6e8}
.f.sub{font-size:8.4px;color:#dfe8f2}
.f.item::before{content:"→ ";color:#6fa0d4;font-size:7px}
.icon-tile{width:30px;height:30px;border-radius:3px;background:#dde3ea;display:flex;align-items:center;justify-content:center}
</style>
</head>
<body>
<header class="abs header">
  <div class="abs brand"><span class="brand-dot"></span><span>KRT <small>INSURE &amp; INVEST</small></span></div>
  <div class="abs nz-map" role="img" aria-label="Small map of New Zealand with a pin on Gisborne"></div>
  <div class="abs region" style="left:356px;top:10px"><b>Sunny Gisborne</b></div>
  <div class="abs region" style="left:343px;top:39px">Servicing clients</div>
  <div class="abs region" style="left:343px;top:54px">New Zealand wide</div>
  <div class="abs tagline">Smart financial decisions for today and for your future<br>Insurances / Investments / Financial Planning<br>0800 555 0142 | 06 555 0143</div>
</header>
<nav class="abs nav">
  <a style="left:70px">Home</a><a style="left:117px">About</a><a style="left:163px">What We Do</a><a style="left:234px">What Life Stage are You?</a><a style="left:355px">Insurances</a><a style="left:420px">Investments</a><a style="left:491px">FAQs</a><a style="left:533px">Consultation</a><a style="left:606px">Contact/Map</a>
</nav>
<div class="abs hero-band"></div>
<div class="abs hero" role="img" aria-label="Team photo: staff and their families standing in front of the office in gumboots"></div>

<section class="abs overview"></section>
<h2 class="abs ov-title" style="left:69px;top:331px">INSURANCE...</h2>
<p class="abs ov-text" style="left:70px;top:360px">An overview of insurance from the point of view of benefits to the customer of working with KRT will be in this space..... Relevant keywords such as the types of insurances e.g. life insurance, travel insurance etc will be mentioned... Should be inviting to both new and current customers....</p>
<div class="abs divider"></div>
<h2 class="abs ov-title" style="left:416px;top:331px">INVESTMENT...</h2>
<p class="abs ov-text" style="left:417px;top:360px">An overview of investments from the point of view of benefits to the customer of working with KRT will be in this space..... Relevant keywords such as financial planning, investment advice and Retirement Saver will be mentioned... Should be inviting to both new and current customers....</p>
<div class="abs btn" style="left:213px;top:429px">
  <svg width="24" height="28" viewBox="0 0 24 28" fill="#fff"><path d="M4 9a8 6 0 0 1 16 0z"/><rect x="11.5" y="9" width="1" height="8"/><circle cx="8" cy="14" r="2.5"/><path d="M5 18h6l-1 10H8l-1-5-2 5H3z"/></svg>
  Find out more...
</div>
<div class="abs btn" style="left:559px;top:429px">
  <svg width="24" height="28" viewBox="0 0 24 28" fill="#fff"><rect x="2" y="18" width="5" height="10"/><rect x="9" y="14" width="5" height="14"/><rect x="16" y="8" width="5" height="20"/><circle cx="18.5" cy="3" r="2.5"/></svg>
  Find out more...
</div>

<h2 class="abs stage-title">What life stage are you at?</h2>
<div class="abs stage-rule"></div>
<div class="abs card" style="left:59px"><h3>18-30 years...</h3>
  <div class="photo" role="img" aria-label="Young couple smiling together" style="background:linear-gradient(#f4eee8,#d9c2ad)"></div>
  <ul><li>Should I start financial planning now?</li><li>What insurances do we need?</li><li>What is the best way to save?</li></ul></div>
<div class="abs card" style="left:227px"><h3>30-45 years...</h3>
  <div class="photo" role="img" aria-label="Family of four outdoors" style="background:linear-gradient(#8fb6dd,#c9a98a)"></div>
  <ul><li>How do we create a balanced financial plan?</li><li>Have we got the right insurance cover?</li><li>WWhich investments are best for us?</li></ul></div>
<div class="abs card" style="left:396px"><h3>45-65 years...</h3>
  <div class="photo" role="img" aria-label="Middle-aged couple in sunglasses under blue sky" style="background:linear-gradient(#5f8fcf,#b59272)"></div>
  <ul><li>Are we on track for retirement savings?</li><li>Is our health insurance cover enough?</li><li>Have we correctly structured our business?</li></ul></div>
<div class="abs card" style="left:565px"><h3>65+ years</h3>
  <div class="photo" role="img" aria-label="Retired couple sharing a meal outdoors" style="background:linear-gradient(#9fb97a,#e6d3b8)"></div>
  <ul><li>Can we take our dream holiday?</li><li>Should we consider downsizing the house?</li><li>How often should we revise our will?</li></ul></div>

<div class="abs form-bg" role="img" aria-label="Soft sky background"></div>
<div class="abs form-tab">
  <svg width="474" height="25" viewBox="0 0 474 25" class="abs" style="left:0;top:0"><path d="M456 0l18 25H456z" fill="#4a5563"/><rect width="456" height="25" fill="#0b3a6e"/></svg>
  <span>Would you like KRT to call you? Fill in the form and we'll be in touch...</span>
</div>
<div class="abs field" style="left:70px;top:842px;width:142px;height:22px">First name:</div>
<div class="abs field" style="left:237px;top:842px;width:141px;height:22px">Last name:</div>
<div class="abs field" style="left:395px;top:842px;width:141px;height:22px">Email:</div>
<div class="abs field" style="left:553px;top:842px;width:140px;height:22px">Contact phone:</div>
<div class="abs field" style="left:70px;top:878px;width:466px;height:53px">Message:</div>
<div class="abs send">SEND</div>

<footer class="abs footer"></footer>
<div class="abs f" style="left:70px;top:964px">Home</div>
<div class="abs f" style="left:70px;top:989px">About</div>
<div class="abs f dim" style="left:70px;top:1002px">--Meet the Team</div>
<div class="abs f dim" style="left:70px;top:1015px">--Testimonials</div>
<div class="abs f" style="left:70px;top:1040px">What We Do</div>
<div class="abs f" style="left:70px;top:1064px">FAQs</div>
<div class="abs f" style="left:70px;top:1089px">Consultation</div>

<div class="abs f" style="left:222px;top:964px">What Life Stage are You?</div>
<div class="abs f dim" style="left:222px;top:992px">--Life stage 18-30 years</div>
<div class="abs f dim" style="left:222px;top:1006px">--Life stage 30-45 years</div>
<div class="abs f dim" style="left:222px;top:1021px">--Life stage 45-65 years</div>
<div class="abs f dim" style="left:222px;top:1036px">--Life stage 65+ years</div>

<div class="abs f" style="left:417px;top:964px">Products/Services</div>
<div class="abs f dim" style="left:417px;top:992px">-- Insurance</div>
<div class="abs f sub item" style="left:431px;top:1008px">Life insurance</div>
<div class="abs f sub item" style="left:431px;top:1023px">Trauma insurance</div>
<div class="abs f sub item" style="left:431px;top:1038px">Disablement cover</div>
<div class="abs f sub item" style="left:431px;top:1053px">Income protection</div>
<div class="abs f sub item" style="left:431px;top:1067px">Health insurance</div>
<div class="abs f sub item" style="left:431px;top:1082px">Business insurance</div>
<div class="abs f sub item" style="left:431px;top:1097px">Fire &amp; General</div>
<div class="abs f sub item" style="left:431px;top:1112px">Travel insurance</div>
<div class="abs f dim" style="left:417px;top:1133px">-- Investment</div>
<div class="abs f sub item" style="left:431px;top:1149px">Retirement Saver</div>

<div class="abs f" style="left:583px;top:964px">Contact/Map</div>
<div class="abs f sub" style="left:586px;top:977px;line-height:12px">27 Kaiti Quay, Gisborne<br>New Zealand<br>PO Box 4410, Gisborne</div>
<div class="abs f sub" style="left:586px;top:1025px">Office Hours: 8.30 – 5pm</div>
<div class="abs f sub" style="left:586px;top:1049px;line-height:12px">After Hours: Please phone:<br>0800 555 0142 | 06 555 0143</div>
<div class="abs icon-tile" style="left:585px;top:1091px" aria-label="Find us">
  <svg width="14" height="20" viewBox="0 0 14 20"><path d="M7 1a6 6 0 0 1 6 6c0 5-6 12-6 12S1 12 1 7a6 6 0 0 1 6-6z" fill="#0b3a6e"/><circle cx="7" cy="7" r="2.2" fill="#dde3ea"/></svg>
</div>
<div class="abs icon-tile" style="left:639px;top:1091px" aria-label="Social page"></div>
<div class="abs footer-base">Copyright © 2014 KRT Insure &amp; Invest | All right reserved.</div>
</body>
</html>
```